New Business Card

We need to refresh our business cards. We designed these ourselves and we have no graphic design experience. We would like to find a new business card design that is professional and unique. We are an auto finance company. Feel free to play with the logo, but we would like to keep the eye very present on the card. Our corporate colors are green, grey, and white.
Green - RGB - 168,215,27; HEX - #AADD22
Grey - RGB - 196,196,196; HEX - #C4C4C4
Updates
Need to upload the vector file to finalize the project. The last logo was for a jpeg that didn't stretch well.
Industry/Entity Type
Financial Service
Contact Information for Business Card
Honestly don't know...I need your help!

```html
<!DOCTYPE html>
<html lang="en">
<head>
<meta charset="utf-8">
<title>Brightlane Capital – Business Card</title>
<link rel="stylesheet" href="https://fonts.googleapis.com/css2?family=Arimo:wght@400;700&display=swap">
<style>
  :root {
    --brand-green: #a8d71b;
    --brand-green-text: #9fd41a;
    --ink: #0b0b0b;
    --paper: #ffffff;
    --backdrop: #ececec;
  }
  * { box-sizing: border-box; margin: 0; padding: 0; }
  html, body { width: 1200px; height: 900px; overflow: hidden; }
  body {
    background: var(--backdrop);
    font-family: "Arimo", Arial, sans-serif;
    color: var(--ink);
    position: relative;
  }
  .card { position: absolute; overflow: hidden; }

  /* Front: green contact side */
  .card-front {
    left: 155px; top: 97px; width: 588px; height: 364px;
    background: var(--brand-green);
  }
  .front-brand {
    position: absolute; left: 28px; top: 120px; width: 270px;
    font-weight: 700; font-size: 38px; line-height: 1.15; color: var(--ink);
  }
  .contact { position: absolute; left: 321px; top: 71px; }
  .contact-name { font-weight: 700; font-size: 22px; line-height: 26px; }
  .contact-role { font-size: 16px; line-height: 20px; }
  .contact-lines { list-style: none; margin-top: 27px; }
  .contact-lines li {
    display: flex; align-items: center; gap: 4px;
    font-size: 16px; line-height: 21px;
  }
  .contact-lines svg { width: 12px; height: 12px; flex: none; }
  .contact-address { margin-top: 20px; font-size: 16px; line-height: 22px; }

  /* Back: white brand side */
  .card-back {
    left: 388px; top: 505px; width: 567px; height: 352px;
    background: var(--paper);
  }
  .back-brand {
    position: absolute; left: 0; right: 0; top: 120px;
    display: flex; flex-direction: column; align-items: center; gap: 24px;
  }
  .brand-dot { width: 24px; height: 24px; border-radius: 50%; background: var(--ink); }
  .brand-name {
    font-weight: 700; font-size: 38px; line-height: 44px;
    color: var(--brand-green-text); letter-spacing: 0.5px;
  }
  .footer-band {
    position: absolute; left: 0; right: 0; bottom: 0; height: 82px;
    background: linear-gradient(180deg, var(--brand-green) 0%, var(--brand-green) 35%, var(--ink) 35%, var(--ink) 100%);
  }
</style>
</head>
<body>

<section class="card card-front">
  <div class="front-brand">Brightlane Capital</div>
  <div class="contact">
    <p class="contact-name">Daniel Harper</p>
    <p class="contact-role">Managing Director</p>
    <ul class="contact-lines">
      <li><svg viewBox="0 0 12 12"><rect x="3" y="0.5" width="6" height="11" rx="1" fill="none" stroke="#0b0b0b" stroke-width="1.4"/><circle cx="6" cy="9.5" r="0.8" fill="#0b0b0b"/></svg>044-555 218 640</li>
      <li><svg viewBox="0 0 12 12"><path d="M1 4 Q6 0 11 4 L10 5.5 L8 4.5 L8 3.6 Q6 3 4 3.6 L4 4.5 L2 5.5Z" fill="#0b0b0b"/><path d="M3 6 L9 6 L10.5 11 L1.5 11Z" fill="#0b0b0b"/></svg>044-555 218 641</li>
      <li><svg viewBox="0 0 12 12"><rect x="1" y="2.5" width="10" height="7" fill="#0b0b0b"/><path d="M1 2.5 L6 6.5 L11 2.5" fill="none" stroke="#a8d71b" stroke-width="1"/></svg>hello@brightlane.com</li>
      <li><svg viewBox="0 0 12 12"><circle cx="6" cy="6" r="5.2" fill="#0b0b0b"/><path d="M1 6 H11 M6 1 Q3.5 6 6 11 M6 1 Q8.5 6 6 11" fill="none" stroke="#a8d71b" stroke-width="0.9"/></svg>www.brightlane.com</li>
    </ul>
    <p class="contact-address">48 Harbour Road, Suite 9<br>Westhaven, 204518.</p>
  </div>
</section>

<section class="card card-back">
  <div class="back-brand">
    <span class="brand-dot"></span>
    <span class="brand-name">Brightlane Capital</span>
  </div>
  <div class="footer-band" role="img" aria-label="Decorative green and black footer band"></div>
</section>

</body>
</html>
```